Illustrate Our Process "Brightpath Method"

We need a graphic design to brand our proprietary process. We are a wealth services team that serves a group of individual and families. Most financial advisors only provide investment management. Our team implements a process that puts our clients goals and finances on a Brightpath foundation.

Please create your own graphic that will simply explain that our elevated process will take care of a client's complete financial picture and in turn put them on a Brightpath foundation.

Our process is called the "Brightpath Method" and it involves:
1) Wealth Management
2) Tax Strategy
3) Cash Management
4) Risk Management
5) Estate Strategy
6) Philanthropy
7) Value Added Services
Note: These things were uploaded in "Brightpath A"

As a person's life becomes more complex they will grow into our process which will constantly ensure their finances & goals are on a Brightpath foundation.

I uploaded pictures of our office so you can see what might go with the overall look and feel of our office if that helps.

Industry/Entity Type

Finance

Requirements
Must have
• The final design should communicate simplicity, stability, expertise and trust. We also want a final design that will quickly describe our process instead of creating confusion.
Nice to have
• We are wanting to put the final design on a canvas print on our bookshelf (which is attached) and have the ability to blow it up and put it on one of our walls.
Should not have
• Clash with the feel and decor of our office

```html
<!DOCTYPE html>
<html lang="en">
<head>
<meta charset="utf-8">
<title>Brightpath Method</title>
<link href="https://fonts.googleapis.com/css2?family=Graduate&display=swap" rel="stylesheet">
<style>
  :root {
    --page: #f3f1f1;
    --panel-center: #3b2868;
    --panel-edge: #1e1647;
    --frame: #ffffff;
    --ink: #1f1b4d;
    --tag-light: #f4f4f4;
    --tag-dark: #d6d6d8;
    --step-1: #8a5bb0;
    --step-2: #5cb87a;
    --step-3: #ee88b8;
    --step-4: #ee8448;
    --step-5: #2bb8d0;
    --step-6: #c0302a;
    --step-7: #9cb25a;
  }
  html, body {
    margin: 0;
    width: 1200px;
    height: 844px;
    overflow: hidden;
    background: var(--page);
  }
  .poster {
    position: absolute;
    left: 0;
    top: 117px;
    width: 1200px;
    height: 610px;
    display: block;
  }
  .step-number {
    font-family: "Graduate", "Rockwell", serif;
    font-size: 18px;
    fill: #ffffff;
    text-anchor: middle;
  }
  .step-label {
    font-family: "Graduate", "Rockwell", serif;
    font-size: 13.5px;
    fill: var(--ink);
    text-anchor: middle;
    letter-spacing: -0.4px;
  }
  .method-title {
    font-family: "Graduate", "Rockwell", serif;
    font-size: 40px;
    fill: #ffffff;
    text-anchor: middle;
  }
</style>
</head>
<body>
<svg class="poster" viewBox="0 0 1200 610" xmlns="http://www.w3.org/2000/svg" aria-label="Brightpath Method: seven steps">
  <defs>
    <radialGradient id="panelGlow" cx="50%" cy="45%" r="70%">
      <stop offset="0" stop-color="var(--panel-center)"/>
      <stop offset="1" stop-color="var(--panel-edge)"/>
    </radialGradient>
    <linearGradient id="tagFill" x1="0" y1="0" x2="0" y2="1">
      <stop offset="0" stop-color="var(--tag-light)"/>
      <stop offset="1" stop-color="var(--tag-dark)"/>
    </linearGradient>
    <g id="tag">
      <polygon points="60,0 236,0 204,60 40,60" fill="url(#tagFill)"/>
    </g>
  </defs>

  <rect class="panel" width="1200" height="610" fill="url(#panelGlow)"/>

  <g class="frame" fill="none" stroke="var(--frame)" stroke-width="2">
    <polyline points="350,438 42,438 42,137 1160,137 1160,438 849,438"/>
  </g>

  <g class="step" transform="translate(225,200)">
    <use href="#tag"/>
    <polygon points="0,0 74,0 38,66" fill="var(--step-1)"/>
    <text class="step-number" x="38" y="28">1.</text>
    <text class="step-label" x="134" y="25">WEALTH</text>
    <text class="step-label" x="134" y="45">MANAGEMENT</text>
  </g>
  <g class="step" transform="translate(486,200)">
    <use href="#tag"/>
    <polygon points="0,0 74,0 38,66" fill="var(--step-2)"/>
    <text class="step-number" x="38" y="28">2.</text>
    <text class="step-label" x="134" y="25">CASH</text>
    <text class="step-label" x="134" y="45">MANAGEMENT</text>
  </g>
  <g class="step" transform="translate(747,200)">
    <use href="#tag"/>
    <polygon points="0,0 74,0 38,66" fill="var(--step-3)"/>
    <text class="step-number" x="38" y="28">3.</text>
    <text class="step-label" x="134" y="25">RISK</text>
    <text class="step-label" x="134" y="45">MANAGEMENT</text>
  </g>

  <g class="step" transform="translate(89,309)">
    <use href="#tag"/>
    <polygon points="0,0 74,0 38,66" fill="var(--step-4)"/>
    <text class="step-number" x="38" y="28">4.</text>
    <text class="step-label" x="134" y="25">TAX</text>
    <text class="step-label" x="134" y="45">STRATEGY</text>
  </g>
  <g class="step" transform="translate(353,309)">
    <use href="#tag"/>
    <polygon points="0,0 74,0 38,66" fill="var(--step-5)"/>
    <text class="step-number" x="38" y="28">5.</text>
    <text class="step-label" x="134" y="25">ESTATE</text>
    <text class="step-label" x="134" y="45">STRATEGY</text>
  </g>
  <g class="step" transform="translate(618,309)">
    <use href="#tag"/>
    <polygon points="0,0 74,0 38,66" fill="var(--step-6)"/>
    <text class="step-number" x="38" y="28">6.</text>
    <text class="step-label" x="134" y="25">VALUE ADDED</text>
    <text class="step-label" x="134" y="45">SERVICES</text>
  </g>
  <g class="step" transform="translate(883,309)">
    <use href="#tag"/>
    <polygon points="0,0 74,0 38,66" fill="var(--step-7)"/>
    <text class="step-number" x="38" y="28">7.</text>
    <text class="step-label" x="134" y="35">PHILANTHROPY</text>
  </g>

  <text class="method-title" x="600" y="454" textLength="470" lengthAdjust="spacingAndGlyphs">BRIGHTPATH METHOD</text>
</svg>
</body>
</html>
```